Logo for Equipment and Auto parts seller
Crestline Supply and Machinery Corporation
Logo for Equipment and Auto parts seller - Automotive
Creative Brief
Simple
Julien Marceau
Operations Manager
Toliso
Julien.Marceau@cslmcorp.net

```html
<!DOCTYPE html>
<html lang="en">
<head>
<meta charset="utf-8">
<title>Crestline Supply and Machinery Corporation – Business Card</title>
<link href="https://fonts.googleapis.com/css2?family=Roboto+Condensed:wght@400;700&family=Montserrat:wght@700&display=swap" rel="stylesheet">
<style>
  :root {
    --backdrop: #cfcfcf;
    --card: #ffffff;
    --brand-blue: #2d3991;
    --brand-green: #78b83a;
    --ink: #3a3a3a;
    --muted: #6b6b6b;
  }
  * { margin: 0; padding: 0; box-sizing: border-box; }
  html, body { width: 1200px; height: 902px; overflow: hidden; }
  body {
    background: var(--backdrop);
    font-family: "Roboto Condensed", Arial, sans-serif;
    color: var(--ink);
    position: relative;
  }
  .card {
    position: absolute;
    left: 260px;
    width: 680px;
    height: 388px;
    background: var(--card);
    box-shadow: 0 6px 18px rgba(0,0,0,0.18);
  }
  .card--back { top: 42px; }
  .card--front { top: 472px; }

  .contact {
    position: absolute;
    top: 40px;
    right: 40px;
    list-style: none;
    text-align: right;
    font-size: 15px;
    line-height: 22px;
  }
  .contact li { display: flex; justify-content: flex-end; align-items: center; gap: 8px; }
  .contact svg { width: 12px; height: 12px; fill: var(--ink); }
  .contact .spacer { width: 12px; }

  .website {
    position: absolute;
    left: 44px;
    bottom: 48px;
    font-size: 17px;
    letter-spacing: 4px;
  }
  .website strong { font-weight: 700; }

  .holder {
    position: absolute;
    right: 44px;
    top: 150px;
    text-align: right;
  }
  .holder__name { color: var(--brand-blue); font-weight: 700; font-size: 24px; }
  .holder__role { color: var(--muted); font-size: 17px; margin-top: 2px; }

  .brand {
    position: absolute;
    left: 44px;
    bottom: 48px;
    display: flex;
    align-items: center;
    gap: 14px;
    width: 360px;
  }
  .brand__dot {
    flex: none;
    width: 44px;
    height: 44px;
    border-radius: 50%;
    background: var(--brand-green);
  }
  .brand__name {
    font-family: "Montserrat", Arial, sans-serif;
    font-weight: 700;
    font-size: 15px;
    line-height: 19px;
    text-transform: uppercase;
    color: var(--brand-blue);
  }
</style>
</head>
<body>
  <section class="card card--back" aria-label="Business card back">
    <ul class="contact">
      <li>2207 Harlow Creek Rd <span class="spacer"></span></li>
      <li>Denton TX 76201
        <svg viewBox="0 0 12 12" aria-hidden="true"><path d="M6 0a4 4 0 0 0-4 4c0 3 4 8 4 8s4-5 4-8a4 4 0 0 0-4-4zm0 5.5A1.5 1.5 0 1 1 6 2.5a1.5 1.5 0 0 1 0 3z"/></svg>
      </li>
      <li>555.014.3928
        <svg viewBox="0 0 12 12" aria-hidden="true"><path d="M2.5 0.5l2 2.5-1.2 1.3a7 7 0 0 0 4.4 4.4L9 7.5l2.5 2-1.3 2C5 11.5 0.5 7 0.5 1.8z"/></svg>
      </li>
      <li>marla@cslmcorp.net
        <svg viewBox="0 0 12 12" aria-hidden="true"><path d="M0 2h12v8H0zM1 3v.4l5 3.3 5-3.3V3z"/></svg>
      </li>
    </ul>
    <p class="website">www.<strong>cslmcorp</strong>.com</p>
  </section>

  <section class="card card--front" aria-label="Business card front">
    <div class="holder">
      <p class="holder__name">Marla Quentin</p>
      <p class="holder__role">Owner</p>
    </div>
    <div class="brand">
      <span class="brand__dot" aria-hidden="true"></span>
      <p class="brand__name">Crestline Supply and Machinery Corporation</p>
    </div>
  </section>
</body>
</html>
```